Esthetically Pleasing Core Values and Brand Promise for Accounting Firm

I would like a cohesive design that ties together my core values and brand promise. My firm, Maple Finch Advisory, provides accounting work to small businesses. I prefer modern and clean designs. I want my Core Values and Brand Promise to represent me - sole entrepreneur, married, mother of two kids, modern esthetics, clean lines, organized, colorful (teals, greys, white, yellows)

Industry/Entity Type

Public Accounting

Colors
33b8a4

```html
<!DOCTYPE html>
<html lang="en">
<head>
<meta charset="utf-8">
<title>Maple Finch Advisory – Core Values</title>
<link rel="stylesheet" href="https://fonts.googleapis.com/css2?family=Montserrat+Alternates:wght@400;500;600&display=swap">
<style>
  :root {
    --backdrop: #4d4d4d;
    --paper: #ffffff;
    --teal: #0b6663;
    --teal-deep: #04504d;
    --teal-brand: #1c9f97;
    --gold: #e8a300;
    --ink-light: #ffffff;
  }
  * { margin: 0; padding: 0; box-sizing: border-box; }
  html, body {
    width: 687px; height: 1200px; overflow: hidden;
    background: var(--backdrop);
    font-family: "Montserrat Alternates", sans-serif;
  }
  .canvas { position: relative; width: 687px; height: 1200px; }
  .banner {
    position: absolute; left: 119px; top: 152px;
    width: 448px; height: 894px;
    background: var(--paper); overflow: hidden;
  }
  .banner-shapes { position: absolute; inset: 0; width: 100%; height: 100%; }
  .brand-name {
    position: absolute; left: 22px; top: 52px; width: 190px;
    display: flex; align-items: center; gap: 7px;
    color: var(--teal-brand); font-size: 14.5px; font-weight: 500;
    line-height: 1; white-space: nowrap;
  }
  .brand-dot {
    width: 11px; height: 11px; border-radius: 50%;
    background: var(--teal-brand); flex: none;
  }
  .section-title {
    position: absolute; color: var(--ink-light); font-weight: 600; line-height: 0.86;
    text-align: right;
  }
  .section-title.core { right: 48px; top: 34px; font-size: 30px; }
  .section-title.promise { right: 180px; top: 481px; font-size: 25.5px; line-height: 0.85; letter-spacing: -0.3px; }
  .value-list {
    position: absolute; list-style: none; color: var(--ink-light);
    font-size: 10.4px; line-height: 14.4px; font-weight: 400;
  }
  .value-list li { position: relative; margin-bottom: 14.5px; }
  .value-list.left li { padding-left: 13px; }
  .value-list.left li::before { content: "•"; position: absolute; left: 0; font-size: 8px; }
  .value-list.set-one { left: 24px; top: 206px; width: 180px; }
  .value-list.set-two { left: 69px; top: 363px; width: 260px; }
  .value-list.right { text-align: right; }
  .value-list.set-three { right: 40px; top: 557px; width: 240px; }
  .value-list.set-four { right: 24px; top: 659px; width: 186px; }
  .bullet-dot { font-size: 8px; margin-right: 8px; vertical-align: 1px; }
</style>
</head>
<body>
<div class="canvas">
  <section class="banner">
    <svg class="banner-shapes" viewBox="0 0 950 1895" preserveAspectRatio="none">
      <defs>
        <clipPath id="teal-field">
          <path d="M0,240 Q40,222 90,238 L455,405 V455 Q462,530 560,565 L950,810 V1755 Q900,1780 850,1745 L495,1515 V1415 Q490,1355 440,1340 L0,1085 Z"/>
        </clipPath>
        <linearGradient id="handshake-tones" x1="0" y1="0" x2="1" y2="1">
          <stop offset="0" stop-color="#6e6a63"/>
          <stop offset="0.45" stop-color="#5a3f2c"/>
          <stop offset="1" stop-color="#3b2a20"/>
        </linearGradient>
        <linearGradient id="chart-tones" x1="0" y1="0" x2="0.6" y2="1">
          <stop offset="0" stop-color="#5b5d5f"/>
          <stop offset="0.45" stop-color="#b9a99a"/>
          <stop offset="0.75" stop-color="#c79a2a"/>
          <stop offset="1" stop-color="#b88a10"/>
        </linearGradient>
      </defs>

      <path d="M465,0 H780 L950,100 V420 L520,170 Q480,170 470,215 L465,225 Z" fill="var(--gold)"/>

      <g clip-path="url(#teal-field)">
        <rect x="0" y="200" width="950" height="1600" fill="var(--teal)"/>
        <path d="M0,335 L950,885 V1010 L0,460 Z" fill="var(--teal-deep)" opacity="0.55"/>
        <path d="M0,460 L950,1010 V1600 L0,935 Z" fill="var(--teal-deep)"/>
        <path d="M0,1000 L950,1560 V1600 L0,1050 Z" fill="var(--teal)" opacity="0.5"/>
      </g>

      <path role="img" aria-label="Photo area: two business people shaking hands over a desk with a signed contract and laptop"
            d="M530,162 L950,405 V790 L560,560 Q478,515 476,460 V215 Q482,150 530,162 Z"
            fill="url(#handshake-tones)"/>

      <path d="M0,1480 L625,1850 Q640,1860 640,1880 V1895 H170 L0,1790 Z" fill="var(--gold)"/>

      <path role="img" aria-label="Photo area: a hand pointing a pen at printed financial bar charts"
            d="M0,1112 L430,1360 Q475,1390 475,1440 V1690 Q470,1750 420,1730 L0,1490 Z"
            fill="url(#chart-tones)"/>
    </svg>

    <div class="brand-name">
      <span class="brand-dot"></span>
      <span>Maple Finch Advisory</span>
    </div>

    <h1 class="section-title core">Core<br>Values</h1>

    <ul class="value-list left set-one">
      <li>Empower – we are dedicated, appreciative and respectful of people's time and purpose.</li>
      <li>Client Focused – we provide a personal service that goes above the standards of professional care.</li>
    </ul>

    <ul class="value-list left set-two">
      <li>Rectitude – we know the difference between what we have the right to do and what the right thing to do is.</li>
      <li>Relentless – we believe that the longer we try to do our best, the better we become.</li>
    </ul>

    <h2 class="section-title promise">Transparency and<br>Dependability</h2>

    <ul class="value-list right set-three">
      <li><span class="bullet-dot">•</span>Tax - Maple Finch provides all clients with a trusted tax advisor who provides accuracy in all filings and ensures your compliance with all government agencies.</li>
    </ul>

    <ul class="value-list right set-four">
      <li><span class="bullet-dot">•</span>Accounting - Maple Finch provides all business owners with the financial visibility needed to foster growth and facilitate goals.</li>
    </ul>
  </section>
</div>
</body>
</html>
```